Business and Success Coaching Business Card

Need a business card for my coaching business. I coach small businesses, career professionals and, individuals wanting to unlock their human potential and achieve excellence. At the heart of our methodology is the Shaping Purposeful Action Routines Knowingly (SPARK) approach to formulate empowerment, create principles for success and setting achievable outcomes. I would like something that incorporates our new logo, something clean and sharp with a solid darker, but complementary background, color on the card front. The back should be white where there will be room for three questions

Target Market(s)

People looking to advance and improve themselves through a success coach

Industry/Entity Type

Life Coaching

Contact Information for Business Card

Contact information on card.
Business name on front of card
Questions on back

Font styles to use
Other font styles liked:
• Century Gothic or other Serif style fonts that look similar to Century Gothic

Colors

Designer to choose colors to be used in the design.

Requirements
Must have
• Logo on front of card
• Business name - The Steady Forge
• Contact name - Ted Harlow
• Address - Box 4619, Littleton, CO 80127-4619
• Phone number - 303-555-0147
• Email address - harlow.ted@thesteadyforge.example
• Certifications - CPC, CHt, MTT, NLPC
• Back of card
• Three questions on the back of the card:
• If you were at your best, what would you do right now?
• What is the decision you have been avoiding?
• What's one action you could take in the next 10 minutes?
Nice to have
• I would like to see a solid color on the front of the card that compliments the logo.
• Back should be white, or could be contrasting, but need to have the three questions.

```html
<!DOCTYPE html>
<html lang="en">
<head>
<meta charset="utf-8">
<title>The Steady Forge – Business Card</title>
<link href="https://fonts.googleapis.com/css2?family=Lato:wght@400;700;900&display=swap" rel="stylesheet">
<style>
  :root {
    --backdrop: #2a2b2e;
    --card: #0a0b0e;
    --edge: #2b4590;
    --brand-blue: #2c4a8f;
    --text-light: #e9ebef;
    --icon: #2f56a6;
  }
  * { box-sizing: border-box; margin: 0; padding: 0; }
  html, body { width: 1200px; height: 970px; overflow: hidden; }
  body {
    background: var(--backdrop);
    font-family: "Lato", Arial, sans-serif;
    position: relative;
  }
  .card {
    position: absolute;
    width: 700px;
    height: 400px;
    background: var(--card);
    border-left: 6px solid var(--edge);
    border-bottom: 6px solid var(--edge);
    box-shadow: 0 18px 40px rgba(0,0,0,.55);
  }
  .card--front { left: 60px; top: 60px; }
  .card--back { left: 440px; top: 510px; }

  .brand { display: flex; align-items: center; justify-content: center; gap: 12px; }
  .brand__dot { width: 18px; height: 18px; border-radius: 50%; background: var(--brand-blue); flex: none; }
  .brand__name {
    color: var(--brand-blue);
    font-weight: 900;
    font-size: 40px;
    letter-spacing: .5px;
    white-space: nowrap;
  }

  .card--front .brand { position: absolute; left: 20px; top: 175px; width: 370px; }
  .card--front .brand__name { font-size: 34px; }

  .divider {
    position: absolute;
    left: 400px; top: 70px;
    width: 2px; height: 250px;
    background: var(--edge);
  }
  .contact { position: absolute; left: 430px; top: 70px; right: 20px; color: var(--text-light); }
  .contact__name { color: var(--brand-blue); font-weight: 900; font-size: 36px; line-height: 1; }
  .contact__creds { font-size: 15px; margin: 6px 0 14px; }
  .contact__address { font-size: 15px; line-height: 1.35; margin-bottom: 12px; }
  .contact__list { list-style: none; }
  .contact__item { display: flex; align-items: center; gap: 10px; font-size: 13.5px; line-height: 1.9; white-space: nowrap; }
  .contact__item svg { width: 14px; height: 14px; flex: none; }

  .card--back .brand { position: absolute; left: 0; right: 0; top: 75px; }
  .questions {
    position: absolute; left: 0; right: 0; top: 200px;
    text-align: center; list-style: none;
    color: var(--text-light); font-size: 22px; line-height: 1.6;
  }
</style>
</head>
<body>
  <section class="card card--front">
    <div class="brand">
      <span class="brand__dot"></span>
      <span class="brand__name">The Steady Forge</span>
    </div>
    <div class="divider"></div>
    <div class="contact">
      <h1 class="contact__name">Ted Harlow</h1>
      <p class="contact__creds">CPC, CHt, MTT, NLPC</p>
      <p class="contact__address">Box 4619, Pinecrest,<br>CO 80127-4619</p>
      <ul class="contact__list">
        <li class="contact__item">
          <svg viewBox="0 0 24 24" fill="var(--icon)"><path d="M6.6 10.8a15 15 0 0 0 6.6 6.6l2.2-2.2a1 1 0 0 1 1-.25 11.4 11.4 0 0 0 3.6.57 1 1 0 0 1 1 1V20a1 1 0 0 1-1 1A17 17 0 0 1 3 4a1 1 0 0 1 1-1h3.5a1 1 0 0 1 1 1c0 1.25.2 2.45.57 3.57a1 1 0 0 1-.25 1z"/></svg>
          303-555-0147
        </li>
        <li class="contact__item">
          <svg viewBox="0 0 24 24" fill="none" stroke="var(--icon)" stroke-width="2"><rect x="3" y="5" width="18" height="14"/><path d="M3 5l9 8 9-8"/></svg>
          harlow.ted@thesteadyforge.example
        </li>
        <li class="contact__item">
          <svg viewBox="0 0 24 24" fill="none" stroke="var(--icon)" stroke-width="2"><circle cx="12" cy="12" r="9"/><path d="M3 12h18M12 3c3 3 3 15 0 18M12 3c-3 3-3 15 0 18"/></svg>
          www.thesteadyforge.example
        </li>
      </ul>
    </div>
  </section>

  <section class="card card--back">
    <div class="brand">
      <span class="brand__dot"></span>
      <span class="brand__name">The Steady Forge</span>
    </div>
    <ul class="questions">
      <li>If you were at your best, what would you do right now?</li>
      <li>What is the decision you have been avoiding?</li>
      <li>What's one action you could take in the next 10 minutes?</li>
    </ul>
  </section>
</body>
</html>
```